Community Legal Website

The website is about a law in legal area (Fiscal), it has a moderator and the community also contributes with information.

Attention that this is not for a Law Firm. This is a community site where all the lawyers can contribute wiith their knowledge and at the same time where they can read the Official Law in the fiscal area.

The site is in portuguese, but we have attach information in english about the functionalities.

I attach information which represents the first version of the site done by html.. That is the site we intend to improve.

The site is quite simple because the main pages are:
- Home page;
- Section page (which has the Chapters and articles)
- Article page;

This pages all belong to the article:

redaccao_actual.htm, redaccoes_anteriores.htm, anotacoes.htm, jurisprudencia.htm, decisoesadministrativas.htm, minutas.htm, duvidas.htm

AS you see in all of them the options are always there.

The most important in this site is the usability of the content:

The FAQ, Contacts, Terms of conditions, who we are, are links less important.

Also there is a possibility to have in the homepage a higligh of certain articles that we want to raise from the others.

Please check the excel sheet as well as the zip file wich has the site in portuguese that you can use a website translator to check in your language.
Updates

We added a excel sheet with the functionalities in english which the site must have.

Reason: Because this is easter time we have increased the time for the deliver

Please check briefing update.

Reason: There were some request to extend the deadline because of the Easter

Hi!

Please read carefully the briefing. People are presenting me company web sites adn this is NOT a company web site. THis is a Site wich has a content of Laws. Please check the 1st version in the zip file and improve it. The options are there and you can translate in google tradutor or reading the excel sheet attach.

txs,
JV

Reason: My client need more desing choices

Target Market(s)

Lawyers, jurists and people related with the fiscal Law.

Industry/Entity Type

Legal

Requirements
Must have
• The interface should be clean and elegant.
It should also contribute to speed.
And try to avoid to many distract elements.
The site will be dinamic and with a backoffice, so in that you have to be carefully with the space dynamic. But you don't have to worry about the backoffice. Only the front office which is the public site.

```html
<!DOCTYPE html>
<html lang="pt">
<head>
<meta charset="utf-8">
<title>Sousa Reis — Legislação Anotada</title>
<link href="https://fonts.googleapis.com/css2?family=PT+Sans:wght@400;700&family=PT+Sans+Narrow:wght@400;700&display=swap" rel="stylesheet">
<style>
:root{
  --ink:#2e2e2e;
  --muted:#6a6a6a;
  --body-text:#7a7a7a;
  --accent:#566e66;
  --accent-link:#4d6a60;
  --header-top:#f2f2f2;
  --header-bottom:#d9d9d9;
  --rule:#d6d6d6;
  --dark:#3a3a3a;
  --darker:#2c2c2c;
  --band:#637d74;
  --page-bg:#ffffff;
}
*{box-sizing:border-box;margin:0;padding:0}
html,body{width:1200px;height:1101px;overflow:hidden;background:var(--page-bg)}
body{position:relative;font-family:"PT Sans",Arial,sans-serif;color:var(--ink)}
.abs{position:absolute}

/* header */
.site-header{position:absolute;left:0;top:0;width:1200px;height:76px;
  background:linear-gradient(var(--header-top),var(--header-bottom));border-top:4px solid var(--dark);
  border-bottom:1px solid #c8c8c8}
.brand{position:absolute;left:308px;top:14px;display:flex;align-items:flex-end;gap:10px}
.brand-mark{width:40px;height:38px;background:var(--dark)}
.brand-name{font-size:17px;font-weight:700;color:var(--accent);letter-spacing:.3px;line-height:1;padding-bottom:0}
.account-tab{position:absolute;left:806px;top:0;width:90px;height:24px;background:var(--dark);
  border-radius:0 0 6px 6px;display:flex;align-items:center;justify-content:space-around;font-size:8px;color:#eee}
.account-tab .login{display:flex;align-items:center;gap:4px}
.account-tab .dot{width:9px;height:9px;border-radius:50%;background:#111;position:relative}
.account-tab .dot:after{content:"";position:absolute;left:3px;top:2px;border-left:4px solid #eee;border-top:2.5px solid transparent;border-bottom:2.5px solid transparent}
.search{position:absolute;left:573px;top:38px;width:293px;height:21px;background:#fff;border:1px solid #bdbdbd;
  box-shadow:inset 0 1px 2px rgba(0,0,0,.12);display:flex;align-items:center}
.search svg{margin:0 6px 0 6px}
.search .sep{width:1px;height:19px;background:#ddd;margin-right:8px}
.search span{font-size:8px;font-style:italic;color:#999}
.search-go{position:absolute;left:868px;top:38px;width:24px;height:21px;background:var(--dark);color:#fff;
  font-size:8px;display:flex;align-items:center;justify-content:center;border-radius:2px}

/* toolbar */
.toolbar{position:absolute;left:0;top:77px;width:1200px;height:40px;border-bottom:1px solid var(--rule)}
.sort{position:absolute;left:307px;top:15px;display:flex;align-items:center;font-size:8px;color:var(--muted)}
.sort .opt{display:flex;align-items:center;gap:6px;margin-left:22px}
.pager{position:absolute;display:flex;height:21px;border:1px solid var(--rule);font-size:8px;color:var(--muted)}
.pager span{display:flex;align-items:center;justify-content:center;min-width:16px;border-left:1px solid var(--rule)}
.pager span:first-child{border-left:0;padding:0 4px}
.pager .current{background:#d8d8d8;color:var(--ink)}

/* sections */
.section-title{position:absolute;left:307px;display:flex;align-items:center;font-family:"PT Sans Narrow",Arial,sans-serif;
  font-size:14.5px;color:var(--ink);letter-spacing:.2px}
.section-title .letter{margin:0 12px 0 10px}
.entry{position:absolute;left:355px;width:540px}
.entry-no{position:absolute;left:0;top:0;font-size:10.5px;color:var(--muted)}
.entry-title{position:absolute;left:51px;top:0;font-size:10.5px;color:var(--ink);white-space:nowrap}
.entry-title.active{text-decoration:underline}
.entry-meta{position:absolute;left:49px;top:16px;width:486px;height:12px;font-size:7px;color:var(--accent-link)}
.entry-meta .author{position:absolute;left:0;display:flex;align-items:center;gap:8px}
.entry-meta .tools{position:absolute;right:0;display:flex;gap:12px}
.entry-meta .tools span{display:flex;align-items:center;gap:5px}
.entry-text{position:absolute;left:51px;top:40px;width:484px;font-size:7.4px;line-height:11.5px;color:var(--body-text)}
.read-more{position:absolute;left:48px;top:82px;width:82px;height:23px;background:var(--accent);color:#fff;border-radius:2px;
  font-size:7.5px;line-height:8.5px;text-align:center;display:flex;align-items:center;justify-content:center}

/* footer */
.site-footer{position:absolute;left:0;top:1052px;width:1200px;height:49px;background:var(--dark);border-top:6px solid var(--band)}
.footer-nav{position:absolute;left:311px;top:17px;display:flex;font-size:8.5px;color:#bbb}
.footer-nav span{padding:0 10px;border-left:1px solid #555}
.footer-nav span:first-child{padding-left:0;border-left:0}
.copyright{position:absolute;left:704px;top:17px;font-size:8.5px;color:#bbb}
</style>
</head>
<body>

<header class="site-header">
  <div class="brand"><div class="brand-mark"></div><div class="brand-name">SOUSA REIS.net</div></div>
  <div class="account-tab"><span class="login">Login <i class="dot"></i></span><span>Register</span></div>
  <div class="search">
    <svg width="11" height="11" viewBox="0 0 11 11"><circle cx="4.5" cy="4.5" r="3.3" fill="none" stroke="#aaa" stroke-width="1.3"/><line x1="7" y1="7" x2="10" y2="10" stroke="#aaa" stroke-width="1.6"/></svg>
    <i class="sep"></i><span>Type search here</span>
  </div>
  <div class="search-go">Go</div>
</header>

<nav class="toolbar">
  <div class="sort">Search by
    <span class="opt" style="margin-left:30px"><svg width="10" height="10" viewBox="0 0 10 10"><circle cx="5" cy="5" r="4" fill="none" stroke="#777" stroke-width="1"/><path d="M5 2.5V5h2" fill="none" stroke="#777"/></svg>Date</span>
    <span class="opt"><svg width="10" height="10" viewBox="0 0 10 10"><rect x="1" y="2" width="7" height="7" fill="none" stroke="#777"/><path d="M4 6l5-5" stroke="#777"/></svg>Title</span>
    <span class="opt"><svg width="10" height="10" viewBox="0 0 10 10"><path d="M1 2h1M1 5h1M1 8h1M4 2h5M4 5h5M4 8h5" stroke="#777"/></svg>Item Number</span>
  </div>
  <div class="pager" style="left:682px;top:10px;width:212px">
    <span>Page 1 of 10</span><span class="current">1</span><span>2</span><span>3</span><span>4</span><span>5</span><span>6</span><span>7</span><span>&rsaquo;</span><span>&raquo;</span><span>Go</span>
  </div>
</nav>

<main>
  <h2 class="section-title" style="top:137px">
    <svg width="18" height="20" viewBox="0 0 18 20"><rect x="2" y="1" width="15" height="18" fill="#444"/><rect x="5" y="5" width="9" height="2" fill="#fff"/><rect x="5" y="9" width="9" height="2" fill="#fff"/><rect x="5" y="13" width="9" height="2" fill="#fff"/><path d="M0 4h3M0 8h3M0 12h3M0 16h3" stroke="#444"/></svg>
    <span class="letter">A.</span>LEGISLAÇÃO FISCAL ANOTADA
  </h2>

  <article class="entry" style="top:181px">
    <div class="entry-no">A. 001</div>
    <h3 class="entry-title">Código do IRS - Imposto sobre o Rendimento das Pessoas Singulares</h3>
    <div class="entry-meta"><span class="author"><svg width="10" height="10" viewBox="0 0 10 10"><circle cx="5" cy="3" r="2.5" fill="#444"/><path d="M0 10c0-4 10-4 10 0z" fill="#444"/></svg>Sousa Reis</span>
      <span class="tools"><span><svg width="11" height="11" viewBox="0 0 11 11"><rect width="11" height="11" fill="#555"/><rect x="2.5" y="1" width="6" height="3.5" fill="#ddd"/></svg>Save as PDF</span><span><svg width="12" height="11" viewBox="0 0 12 11"><rect x="3" y="0" width="6" height="3" fill="#555"/><rect x="0" y="3" width="12" height="5" fill="#555"/><rect x="3" y="7" width="6" height="4" fill="#999"/></svg>Print</span></span></div>
    <p class="entry-text">Ut wisi enim ad minim veniam, quis nostrud exerci tation ullamcorper suscipit lobortis nisl ut aliquip ex ea commodo consequat. Duis autem vel eum iriure dolor in hendrerit in vulputate velit esse molestie consequat, vel illum dolore eu feugiat nulla facilisis at vero eros et accumsan et iusto odio dignissim qui blandit praesent ....</p>
    <div class="read-more">Clique aqui para<br>ler o texto integra</div>
  </article>

  <article class="entry" style="top:319px">
    <div class="entry-no">A. 002</div>
    <h3 class="entry-title active">Código do IRC - Imposto sobre o Rendimento das Pessoas Colectivas</h3>
    <div class="entry-meta"><span class="author"><svg width="10" height="10" viewBox="0 0 10 10"><circle cx="5" cy="3" r="2.5" fill="#444"/><path d="M0 10c0-4 10-4 10 0z" fill="#444"/></svg>Sousa Reis</span>
      <span class="tools"><span><svg width="11" height="11" viewBox="0 0 11 11"><rect width="11" height="11" fill="#555"/><rect x="2.5" y="1" width="6" height="3.5" fill="#ddd"/></svg>Save as PDF</span><span><svg width="12" height="11" viewBox="0 0 12 11"><rect x="3" y="0" width="6" height="3" fill="#555"/><rect x="0" y="3" width="12" height="5" fill="#555"/><rect x="3" y="7" width="6" height="4" fill="#999"/></svg>Print</span></span></div>
    <p class="entry-text">Ut wisi enim ad minim veniam, quis nostrud exerci tation ullamcorper suscipit lobortis nisl ut aliquip ex ea commodo consequat. Duis autem vel eum iriure dolor in hendrerit in vulputate velit esse molestie consequat, vel illum dolore eu feugiat nulla facilisis at vero eros et accumsan et iusto odio dignissim qui blandit praesent ....</p>
    <div class="read-more">Clique aqui para<br>ler o texto integra</div>
  </article>

  <article class="entry" style="top:464px">
    <div class="entry-no">A. 003</div>
    <h3 class="entry-title">Código do IMI - Imposto Municipal sobre Imóveis</h3>
    <div class="entry-meta"><span class="author"><svg width="10" height="10" viewBox="0 0 10 10"><circle cx="5" cy="3" r="2.5" fill="#444"/><path d="M0 10c0-4 10-4 10 0z" fill="#444"/></svg>Sousa Reis</span>
      <span class="tools"><span><svg width="11" height="11" viewBox="0 0 11 11"><rect width="11" height="11" fill="#555"/><rect x="2.5" y="1" width="6" height="3.5" fill="#ddd"/></svg>Save as PDF</span><span><svg width="12" height="11" viewBox="0 0 12 11"><rect x="3" y="0" width="6" height="3" fill="#555"/><rect x="0" y="3" width="12" height="5" fill="#555"/><rect x="3" y="7" width="6" height="4" fill="#999"/></svg>Print</span></span></div>
    <p class="entry-text">Ut wisi enim ad minim veniam, quis nostrud exerci tation ullamcorper suscipit lobortis nisl ut aliquip ex ea commodo consequat. Duis autem vel eum iriure dolor in hendrerit in vulputate velit esse molestie consequat, vel illum dolore eu feugiat nulla facilisis at vero eros et accumsan et iusto odio dignissim qui blandit praesent ....</p>
    <div class="read-more">Clique aqui para<br>ler o texto integra</div>
  </article>

  <article class="entry" style="top:612px">
    <div class="entry-no">A. 004</div>
    <h3 class="entry-title">RCPIT - Regulamento Complementar do Procedimento de Inspecção Tributária</h3>
    <div class="entry-meta"><span class="author"><svg width="10" height="10" viewBox="0 0 10 10"><circle cx="5" cy="3" r="2.5" fill="#444"/><path d="M0 10c0-4 10-4 10 0z" fill="#444"/></svg>Sousa Reis</span>
      <span class="tools"><span><svg width="11" height="11" viewBox="0 0 11 11"><rect width="11" height="11" fill="#555"/><rect x="2.5" y="1" width="6" height="3.5" fill="#ddd"/></svg>Save as PDF</span><span><svg width="12" height="11" viewBox="0 0 12 11"><rect x="3" y="0" width="6" height="3" fill="#555"/><rect x="0" y="3" width="12" height="5" fill="#555"/><rect x="3" y="7" width="6" height="4" fill="#999"/></svg>Print</span></span></div>
    <p class="entry-text" style="top:46px">Ut wisi enim ad minim veniam, quis nostrud exerci tation ullamcorper suscipit lobortis nisl ut aliquip ex ea commodo consequat. Duis autem vel eum iriure dolor in hendrerit in vulputate velit esse molestie consequat, vel illum dolore eu feugiat nulla facilisis at vero eros et accumsan et iusto odio dignissim qui blandit praesent ....</p>
    <div class="read-more" style="top:89px">Clique aqui para<br>ler o texto integra</div>
  </article>

  <h2 class="section-title" style="top:785px">
    <svg width="18" height="20" viewBox="0 0 18 20"><rect x="2" y="1" width="15" height="18" fill="#444"/><rect x="5" y="5" width="9" height="2" fill="#fff"/><rect x="5" y="9" width="9" height="2" fill="#fff"/><rect x="5" y="13" width="9" height="2" fill="#fff"/><path d="M0 4h3M0 8h3M0 12h3M0 16h3" stroke="#444"/></svg>
    <span class="letter">B.</span>LEGISLAÇÃO ADMINISTRATIVA ANOTADA
  </h2>

  <article class="entry" style="top:831px">
    <div class="entry-no" style="left:2px">B. 001</div>
    <h3 class="entry-title">CPTA - Código do Procedimento nos Tribunais Administrativos</h3>
    <div class="entry-meta"><span class="author"><svg width="10" height="10" viewBox="0 0 10 10"><circle cx="5" cy="3" r="2.5" fill="#444"/><path d="M0 10c0-4 10-4 10 0z" fill="#444"/></svg>Sousa Reis</span>
      <span class="tools"><span><svg width="11" height="11" viewBox="0 0 11 11"><rect width="11" height="11" fill="#555"/><rect x="2.5" y="1" width="6" height="3.5" fill="#ddd"/></svg>Save as PDF</span><span><svg width="12" height="11" viewBox="0 0 12 11"><rect x="3" y="0" width="6" height="3" fill="#555"/><rect x="0" y="3" width="12" height="5" fill="#555"/><rect x="3" y="7" width="6" height="4" fill="#999"/></svg>Print</span></span></div>
    <p class="entry-text" style="top:46px">Ut wisi enim ad minim veniam, quis nostrud exerci tation ullamcorper suscipit lobortis nisl ut aliquip ex ea commodo consequat. Duis autem vel eum iriure dolor in hendrerit in vulputate velit esse molestie consequat, vel illum dolore eu feugiat nulla facilisis at vero eros et accumsan et iusto odio dignissim qui blandit praesent ....</p>
    <div class="read-more" style="top:89px">Clique aqui para<br>ler o texto integra</div>
  </article>

  <div class="pager" style="left:306px;top:992px;width:212px">
    <span>Page 1 of 10</span><span class="current">1</span><span>2</span><span>3</span><span>4</span><span>5</span><span>6</span><span>7</span><span>&rsaquo;</span><span>&raquo;</span><span>Go</span>
  </div>
</main>

<footer class="site-footer">
  <nav class="footer-nav"><span>Índice deste Código</span><span>Menu dos Códigos</span><span>Gravar</span><span>Imprimir</span></nav>
  <div class="copyright">Copyright © 2013 SOUSA REIS All Right Reserved</div>
</footer>

</body>
</html>
```